Dorral Fitness fitness and wellness for 50+ and youth

We are a fitness company that caters to 50+ wellness and youth conditioning. Our motto is "We make fitness fun". We offer online wellness programs that include bootcamp style workouts as well as nutrition information/guidance. We would like a design that integrates our logo as well as bring attention to the FUN aspect of being healthy.

Target Market(s)

50+ and parents of teens & tweens

Industry/Entity Type

Fitness

Requirements
Must have
• Topic boxes
Nice to have
• Semi transparent grey or black header with logo integrated

```html
<!DOCTYPE html>
<html lang="en">
<head>
<meta charset="utf-8">
<title>Dorral Fitness</title>
<link href="https://fonts.googleapis.com/css2?family=Lato:wght@400;700;900&display=swap" rel="stylesheet">
<style>
:root{
  --green:#2fbf1f;
  --green-dark:#1e8f12;
  --green-deep:#167a0c;
  --black:#0d0d0d;
  --charcoal:#1b1b1b;
  --grey-box:#a9a9a9;
  --grey-text:#555;
  --white:#fff;
}
*{margin:0;padding:0;box-sizing:border-box}
html,body{width:744px;height:1200px;overflow:hidden}
body{font-family:'Lato',Arial,sans-serif;background:var(--white);color:var(--grey-text)}
.page{width:744px;height:1200px;position:relative;overflow:hidden}
.wrap{width:520px;margin:0 auto}

.site-header{height:60px;background:var(--black);display:flex;align-items:center}
.brand{display:flex;align-items:center;gap:8px;margin-left:112px}
.brand-dot{width:22px;height:22px;border-radius:50%;background:var(--green)}
.brand-name{color:var(--white);font-weight:900;font-size:22px;letter-spacing:.5px}

.main-nav{height:22px;background:linear-gradient(var(--green),var(--green-dark))}
.main-nav ul{list-style:none;display:flex;justify-content:center;height:100%}
.main-nav li{color:var(--white);font-size:8px;font-weight:700;padding:0 11px;display:flex;align-items:center;letter-spacing:.3px}
.main-nav li.active{background:var(--green-deep)}

.hero{height:300px;position:relative;background:linear-gradient(100deg,#6b6b6b 0%,#9a9a9a 35%,#d4d4d4 60%,#8a8a8a 100%)}
.hero-caption{position:absolute;left:118px;top:118px}
.hero-title{background:rgba(0,0,0,.6);color:var(--white);font-weight:900;font-size:20px;padding:6px 10px;display:inline-block}
.hero-sub{background:var(--green);color:var(--white);font-size:9px;font-weight:700;padding:4px 10px;display:block;width:max-content;margin-top:2px}
.hero-dots{position:absolute;bottom:10px;left:50%;transform:translateX(-50%);display:flex;gap:5px}
.hero-dots span{width:7px;height:7px;border-radius:50%;background:rgba(255,255,255,.6)}
.hero-dots span.on{background:var(--white)}

.welcome{height:138px;padding-top:24px;text-align:center}
.welcome h1{font-size:17px;font-weight:900;color:#222;letter-spacing:.3px}
.welcome p{font-size:7.5px;line-height:1.6;margin-top:12px;color:#666}
.welcome p+p{margin-top:8px}

.topics{height:195px;background:var(--black);padding-top:22px}
.topic-row{display:flex;gap:10px;width:520px;margin:0 auto}
.topic{flex:1;height:150px;background:var(--grey-box);color:var(--white);text-align:center;padding:12px 10px}
.topic.featured{background:var(--green)}
.topic-icon{width:30px;height:30px;border-radius:50%;background:rgba(255,255,255,.25);margin:0 auto;display:flex;align-items:center;justify-content:center}
.topic h3{font-size:10px;font-weight:700;margin-top:8px}
.topic p{font-size:7px;line-height:1.5;margin-top:6px}
.btn{display:inline-block;background:var(--charcoal);color:var(--white);font-size:6.5px;font-weight:700;padding:4px 7px;margin-top:9px}

.features{height:210px;padding-top:22px}
.feature-row{display:flex;gap:20px;width:520px;margin:0 auto}
.feature{flex:1}
.feature-photo{height:72px}
.photo-why{background:linear-gradient(135deg,#7fc65a,#d9e8c4)}
.photo-online{background:linear-gradient(135deg,#c0392b,#e9c46a,#7ba05b)}
.photo-events{background:linear-gradient(135deg,#f2d16b,#9bbf4c)}
.feature h3{font-size:10px;font-weight:900;color:#222;margin-top:10px}
.feature p{font-size:7px;line-height:1.5;margin-top:5px;color:#666}
.feature .btn{background:var(--green)}

.videos{height:205px;background:linear-gradient(var(--green),var(--green-dark));padding-top:20px}
.videos h2{text-align:center;color:var(--white);font-size:15px;font-weight:900;letter-spacing:.5px}
.video-row{display:flex;gap:12px;width:520px;margin:16px auto 0}
.video{flex:1;color:var(--white)}
.video-thumb{height:75px;position:relative;display:flex;align-items:center;justify-content:center}
.thumb-a{background:linear-gradient(135deg,#3a3a3a,#8a7a6a)}
.thumb-b{background:linear-gradient(135deg,#5a4a3a,#b09070)}
.thumb-c{background:linear-gradient(135deg,#6aa0c8,#e0e0e0)}
.thumb-d{background:linear-gradient(135deg,#4a4a4a,#a0a0a0)}
.play{position:absolute}
.video h4{font-size:8px;font-weight:700;margin-top:6px}
.video p{font-size:7px;line-height:1.4;margin-top:2px}

.site-footer{height:70px;background:var(--black);color:var(--white)}
.footer-inner{width:520px;margin:0 auto;padding-top:18px;display:flex;justify-content:space-between}
.footer-nav{font-size:7.5px;font-weight:700;letter-spacing:.3px}
.footer-nav span{margin-right:4px}
.copyright{font-size:6.5px;color:#999;margin-top:6px}
.social{display:flex;gap:6px}
.social span{width:11px;height:11px;border-radius:50%;background:var(--white)}
</style>
</head>
<body>
<div class="page">

<header class="site-header">
  <div class="brand"><span class="brand-dot"></span><span class="brand-name">Dorral Fitness</span></div>
</header>

<nav class="main-nav">
  <ul>
    <li class="active">HOME</li><li>VIDEO TIPS</li><li>GALLERY</li><li>ARCHIVES</li><li>UPCOMING EVENTS</li><li>LINKS</li><li>CONTACT US</li>
  </ul>
</nav>

<section class="hero" role="img" aria-label="Woman training with dumbbells beside a coach in a gym">
  <div class="hero-caption">
    <div class="hero-title">WE MAKE FITNESS FUN</div>
    <div class="hero-sub">GET MOVING AND SMILE EVERY DAY</div>
  </div>
  <div class="hero-dots"><span></span><span class="on"></span><span></span></div>
</section>

<section class="welcome">
  <div class="wrap">
    <h1>WELCOME TO DORRAL FITNESS MAINPAGE</h1>
    <p>Dorral Fitness brings simple, joyful movement to adults over fifty and to busy teens and tweens. Our coaches build friendly online sessions that mix strength, balance and cardio with plenty of laughter, so every workout feels like time with good friends rather than a chore you have to finish.</p>
    <p>Parents can join their kids, grandparents can move at their own pace, and everyone gets clear nutrition tips to keep the energy going all week long.</p>
  </div>
</section>

<section class="topics">
  <div class="topic-row">
    <div class="topic featured">
      <div class="topic-icon"><svg width="16" height="16" viewBox="0 0 16 16"><rect x="1" y="6" width="3" height="4" fill="#fff"/><rect x="12" y="6" width="3" height="4" fill="#fff"/><rect x="4" y="7.3" width="8" height="1.4" fill="#fff"/></svg></div>
      <h3>Bootcamp Style</h3>
      <p>Short group circuits that build strength and stamina while keeping every session upbeat.</p>
      <span class="btn">Read More</span>
    </div>
    <div class="topic">
      <div class="topic-icon"><svg width="16" height="16" viewBox="0 0 16 16"><circle cx="8" cy="8" r="5" fill="none" stroke="#fff" stroke-width="1.5"/><path d="M8 5v3l2 2" stroke="#fff" stroke-width="1.5" fill="none"/></svg></div>
      <h3>Workouts</h3>
      <p>Guided routines for every level, from gentle mobility to fast interval training.</p>
      <span class="btn">Read More</span>
    </div>
    <div class="topic">
      <div class="topic-icon"><svg width="16" height="16" viewBox="0 0 16 16"><circle cx="8" cy="9" r="5" fill="#fff"/><path d="M8 4c0-2 2-3 3-3" stroke="#fff" stroke-width="1.2" fill="none"/></svg></div>
      <h3>Nutrition Information</h3>
      <p>Easy meal ideas and smart food choices that support your goals each day.</p>
      <span class="btn">Read More</span>
    </div>
    <div class="topic">
      <div class="topic-icon"><svg width="16" height="16" viewBox="0 0 16 16"><path d="M3 8l3 3 7-7" stroke="#fff" stroke-width="2" fill="none"/></svg></div>
      <h3>Guidance</h3>
      <p>Friendly coaches who answer questions and keep you motivated along the way.</p>
      <span class="btn">Read More</span>
    </div>
  </div>
</section>

<section class="features">
  <div class="feature-row">
    <article class="feature">
      <div class="feature-photo photo-why" role="img" aria-label="Smiling family exercising outdoors"></div>
      <h3>WHY CHOOSE US</h3>
      <p>Caring coaches, fun classes and programs shaped for every age and ability.</p>
      <span class="btn">Read More</span>
    </article>
    <article class="feature">
      <div class="feature-photo photo-online" role="img" aria-label="Fresh vegetables and healthy food on a table"></div>
      <h3>ONLINE WELLNESS PROGRAM</h3>
      <p>Train from home with live and recorded sessions built around your schedule.</p>
      <span class="btn">Read More</span>
    </article>
    <article class="feature">
      <div class="feature-photo photo-events" role="img" aria-label="Group jogging in a sunny park"></div>
      <h3>UPCOMING EVENTS</h3>
      <p>Join our family walks, park bootcamps and healthy cooking nights this season.</p>
      <span class="btn">Read More</span>
    </article>
  </div>
</section>

<section class="videos">
  <h2>LATEST VIDEO TIPS</h2>
  <div class="video-row">
    <div class="video">
      <div class="video-thumb thumb-a" role="img" aria-label="Video still of a stretching session"><svg class="play" width="22" height="22" viewBox="0 0 22 22"><circle cx="11" cy="11" r="10" fill="rgba(255,255,255,.85)"/><path d="M9 6.5l6 4.5-6 4.5z" fill="#222"/></svg></div>
      <h4>Morning stretch routine</h4>
      <p>Quick tips to start your day with energy.</p>
    </div>
    <div class="video">
      <div class="video-thumb thumb-b" role="img" aria-label="Video still of a balance exercise"><svg class="play" width="22" height="22" viewBox="0 0 22 22"><circle cx="11" cy="11" r="10" fill="rgba(255,255,255,.85)"/><path d="M9 6.5l6 4.5-6 4.5z" fill="#222"/></svg></div>
      <h4>Balance for beginners</h4>
      <p>Simple moves to steady every step.</p>
    </div>
    <div class="video">
      <div class="video-thumb thumb-c" role="img" aria-label="Video still of outdoor agility drills"><svg class="play" width="22" height="22" viewBox="0 0 22 22"><circle cx="11" cy="11" r="10" fill="rgba(255,255,255,.85)"/><path d="M9 6.5l6 4.5-6 4.5z" fill="#222"/></svg></div>
      <h4>Teen agility drills</h4>
      <p>Fast footwork games for young athletes.</p>
    </div>
    <div class="video">
      <div class="video-thumb thumb-d" role="img" aria-label="Video still of healthy snacks"><svg class="play" width="22" height="22" viewBox="0 0 22 22"><circle cx="11" cy="11" r="10" fill="rgba(255,255,255,.85)"/><path d="M9 6.5l6 4.5-6 4.5z" fill="#222"/></svg></div>
      <h4>Healthy snack ideas</h4>
      <p>Fuel up with tasty bites after class.</p>
    </div>
  </div>
</section>

<footer class="site-footer">
  <div class="footer-inner">
    <div>
      <div class="footer-nav"><span>HOME</span>|<span> ARCHIVES</span>|<span> VIDEO TIPS</span>|<span> GALLERY</span>|<span> UPCOMING EVENTS</span>|<span> CONTACT US</span></div>
      <div class="copyright">© 2024 Dorral Fitness. All rights reserved.</div>
    </div>
    <div class="social"><span></span><span></span><span></span><span></span></div>
  </div>
</footer>

</div>
</body>
</html>
```